Landing Page für Pruefkiel-Schnell.de
Zielgruppe
Domain: Pruefkiel-Schnell.de
THC Schnelltests mit gringer Anzeigegrenze mit 5ng/ml, ausgerichtet auf die Selbstkontrolle für die Fahrtauglichkeit (Grenze im Gesetz 3,5ng/ml)
Farbe: grün
Anregung siehe Bild
Aufgabenstellung
- Conversionoptimiert
- Soll auf unseren Webshop www.vr-pharmo.de verlinken

```html
<!DOCTYPE html>
<html lang="de">
<head>
<meta charset="utf-8">
<title>Pruefkiel-Schnell.de – THC Schnelltests</title>
<link rel="stylesheet" href="https://fonts.googleapis.com/css2?family=Montserrat:ital,wght@0,700;0,800;0,900;1,600;1,700;1,800;1,900&display=swap">
<style>
  :root {
    --stage-bg: #a7c198;
    --panel-top: #0b3f0b;
    --panel-bottom: #4b8449;
    --cream: #f6f0d8;
    --badge-cream: #fdf0c2;
    --lime: #8fdc5a;
    --button-green: #9be05a;
    --button-shade: #2c5a27;
    --text-dark: #1d461c;
    --badge-text: #3b7a36;
    --dot: #86c45e;
  }
  * { box-sizing: border-box; margin: 0; padding: 0; }
  html, body { width: 1200px; height: 1117px; overflow: hidden; }
  body { background: var(--stage-bg); font-family: "Montserrat", sans-serif; position: relative; }

  .banner {
    position: absolute; left: 64px; top: 374px; width: 1072px; height: 368px;
    overflow: hidden;
    box-shadow: 6px 8px 10px rgba(40, 70, 35, 0.35);
  }
  .banner__photo {
    position: absolute; inset: 0;
    background: radial-gradient(ellipse at 30% 45%, #6f8f3c 0%, #2f5a22 30%, #16301a 65%, #0d2212 100%);
  }
  .banner__panel { position: absolute; inset: 0; }
  .banner__product {
    position: absolute; left: 280px; top: 40px; width: 330px; height: 310px;
    border-radius: 20px;
    background: linear-gradient(160deg, rgba(240,242,244,0.85), rgba(215,222,226,0.55));
    transform: rotate(-8deg);
  }

  .headline {
    position: absolute; right: 42px; top: 20px;
    text-align: right; color: var(--cream);
    font-weight: 900; font-style: italic; font-size: 69px; line-height: 64px;
    letter-spacing: -0.5px;
    text-shadow: 2px 3px 4px rgba(0,0,0,0.3);
  }
  .warning {
    position: absolute; right: 56px; top: 162px;
    color: var(--lime); font-weight: 800; font-style: italic; font-size: 16.5px;
  }
  .product-title {
    position: absolute; right: 54px; top: 190px;
    color: var(--cream); font-weight: 900; font-style: italic; font-size: 27px;
    text-shadow: 1px 2px 3px rgba(0,0,0,0.25);
  }
  .product-desc {
    position: absolute; left: 732px; width: 280px; top: 225px;
    text-align: center; color: var(--cream);
    font-weight: 600; font-style: italic; font-size: 12px; line-height: 16px;
  }
  .cta {
    position: absolute; left: 746px; top: 295px; width: 254px; height: 42px;
    border-radius: 7px; background: var(--button-green);
    box-shadow: 0 5px 0 var(--button-shade);
    display: flex; align-items: center; justify-content: center;
    color: var(--text-dark); font-weight: 900; font-size: 24px; letter-spacing: 0.5px;
    text-decoration: none;
  }
  .limit-badge {
    position: absolute; left: 562px; top: 204px; width: 148px; height: 148px;
    border-radius: 50%; background: var(--badge-cream);
    box-shadow: 0 4px 8px rgba(0,0,0,0.25);
    display: flex; align-items: center; justify-content: center; text-align: center;
    color: var(--badge-text); font-weight: 800; font-style: italic; font-size: 20px; line-height: 23px;
  }
</style>
</head>
<body>
  <section class="banner">
    <div class="banner__photo" role="img" aria-label="Nahaufnahme einer blühenden Cannabispflanze"></div>

    <svg class="banner__panel" width="1072" height="368" viewBox="0 0 1072 368" aria-hidden="true">
      <defs>
        <linearGradient id="panelGradient" x1="0" y1="0" x2="0" y2="1">
          <stop offset="0" stop-color="var(--panel-top)"/>
          <stop offset="1" stop-color="var(--panel-bottom)"/>
        </linearGradient>
      </defs>
      <polygon points="497,0 1072,0 1072,368 389,368 229,204" fill="url(#panelGradient)"/>
      <g fill="var(--dot)">
        <circle cx="515" cy="25" r="2.5"/>
        <circle cx="597" cy="34" r="4"/>
        <circle cx="538" cy="62" r="6.5"/>
        <circle cx="274" cy="220" r="9"/>
        <circle cx="332" cy="278" r="2.5"/>
        <circle cx="388" cy="292" r="5"/>
        <circle cx="423" cy="319" r="3"/>
        <circle cx="406" cy="348" r="2.5"/>
      </g>
    </svg>

    <div class="banner__product" role="img" aria-label="THC-Schnelltest-Set mit Beutel, Testkassette, Pipette und Trockenmittel"></div>

    <h1 class="headline">MACH DEN<br>SELBSTTEST.</h1>
    <p class="warning">GEFÄHRDE NICHT DEINEN FÜHRERSCHEIN!</p>
    <h2 class="product-title">THC SCHNELLTESTS</h2>
    <p class="product-desc">MIT GRINGER ANZEIGEGRENZE<br>MIT 5NG/ML, AUSGERICHTET AUF DIE<br>SELBSTKONTROLLE FÜR DIE<br>FAHRTAUGLICHKEIT</p>
    <div class="limit-badge">Grenze<br>im Gesetz<br>3,5ng/ml</div>
    <a class="cta" href="https://www.vr-pharmo.de">JETZT PRÜFEN</a>
  </section>
</body>
</html>
```